Stop Clapping - Get A Job (Attention Grabbing Billboard Design)

We wish to design a moving bill-board for jobs as Community Support Workers
On paper adverts - the job adverts reads:
Are you looking for a role with variety
Are you looking to make a difference to people's lives
Find out more about us at www.kestrelpathlimited.co.uk
Kestrel Path Ltd supports young adults with disabilities that may include learning, physical, and mental health, to live in the community as independently as possible. Our main objective is for these young adults to realise their life's desires, goals and aspirations.
Kestrel Path Ltd are looking for energetic individuals with a caring heart, who can combine their own initiatives, bright personality and a sense of humor to be the Support Worker to such young adults. Work is in 12hour shifts around the clock and any day of the week.
Fully paid training shall be provided although previous experience is desirable and an advantage.
Please send us your cv and a covering letter and we shall be happy to get in touch with you asap. Please note if successful applicants will be subject to a full QTR check.
Part-time hours: 60 per week
Job Types: Full-time, Part-time, Permanent
Salary: £9.00-£11.00 per hour
Schedule:
12 hour shift
Day shift
Monday to Friday
Night shift
Weekends
Experience:
Support Environment: 1 year (Preferred)
Location:
Chatham ZX9 2LP (Preferred)
Licence:
BWK Level 2 Health & Social Care (Preferred)
Work remotely:
No
www.kestrelpathlimited.co.uk
support@kestrelpathgroup.co.uk
Telephone: 0800 712 4093
Target Market(s)
jobless people
employed people looking to make a change to social care
community leaders so they can appreciate the efforts we are making to keeping vulnerable people in the community and out of the GVL therefore saving lives and protecting the GVL
Requirements
Must have
- We are looking for an attention grabbing billboard as this shall be on the side of local buses and on a couple of vans

```html
<!DOCTYPE html>
<html lang="en">
<head>
<meta charset="utf-8">
<title>Stop Clapping – Join the Frontline | Kestrel Path</title>
<link href="https://fonts.googleapis.com/css2?family=Poppins:wght@600;700;800&family=Barlow+Condensed:wght@500&display=swap" rel="stylesheet">
<style>
  :root{
    --stage:#716f70;
    --white:#ffffff;
    --navy:#143c5e;
    --blue:#23679a;
    --sky:#5aa6dc;
    --gold:#e0a00a;
    --orange:#e29a0c;
    --ink:#222222;
    --rule:#1a9a7a;
  }
  *{margin:0;padding:0;box-sizing:border-box}
  html,body{width:1200px;height:1000px;overflow:hidden;background:var(--stage)}
  .billboard{position:absolute;left:40px;top:238px;width:1123px;height:445px;overflow:hidden;background:var(--white);font-family:"Poppins",sans-serif}
  .billboard-shapes{position:absolute;inset:0}
  .accent-bar{position:absolute;left:44px;top:47px;width:5px;height:94px;background:var(--gold)}
  .headline{position:absolute;left:70px;top:40px;font-weight:800;font-size:51px;line-height:60px;letter-spacing:.3px;white-space:nowrap}
  .headline .lead{color:var(--gold);display:block;letter-spacing:4.8px}
  .headline .strong{color:var(--navy);display:block}
  .divider{position:absolute;left:42px;top:171px;width:564px;height:2px;background:var(--gold)}
  .role{position:absolute;left:42px;top:190px;font-weight:600;font-size:28px;letter-spacing:1.2px;color:var(--ink);line-height:34px;white-space:nowrap}
  .cta-line{position:absolute;left:42px;top:222px;font-weight:800;font-size:33px;letter-spacing:.5px;color:var(--navy);line-height:40px;white-space:nowrap}
  .more-pill{position:absolute;left:42px;top:292px;width:485px;height:48px;border-radius:0 14px 14px 0;background:var(--orange);color:var(--white);font-weight:700;font-size:30px;line-height:48px;padding-left:13px;white-space:nowrap}
  .phone{position:absolute;left:40px;top:360px;display:flex;align-items:center;gap:18px;color:var(--white);font-family:"Barlow Condensed",sans-serif;font-weight:500;font-size:54px;line-height:54px;white-space:nowrap}
  .contact-rule{position:absolute;left:396px;top:366px;width:2px;height:44px;background:var(--rule)}
  .contacts{position:absolute;left:425px;top:357px;color:var(--white);font-family:"Barlow Condensed",sans-serif;font-weight:500;font-size:21px;line-height:26px;list-style:none;white-space:nowrap}
  .contacts li{display:flex;align-items:center;gap:12px}
  .photo{position:absolute;left:656px;top:21px;width:376px;height:376px;border-radius:50%;background:radial-gradient(circle at 50% 45%,#f2f3f5 0%,#d9dcdf 70%,#c8ccd0 100%)}
  .brand{position:absolute;left:766px;top:46px;display:flex;align-items:center;gap:8px;color:var(--navy);font-weight:700;font-size:25px;line-height:30px;white-space:nowrap}
  .brand-dot{width:22px;height:22px;border-radius:50%;background:var(--blue)}
</style>
</head>
<body>
<section class="billboard">
  <svg class="billboard-shapes" width="1123" height="445" viewBox="0 0 1123 445">
    <defs>
      <linearGradient id="handleGrad" x1="0" y1="0" x2="1" y2="1">
        <stop offset="0" stop-color="#e6a800"/>
        <stop offset="1" stop-color="#f6ee00"/>
      </linearGradient>
      <linearGradient id="ringGrad" x1="0" y1="0" x2="1" y2="1">
        <stop offset="0" stop-color="#e2a000"/>
        <stop offset="1" stop-color="#f2d800"/>
      </linearGradient>
    </defs>
    <path d="M0 258 C180 245 470 285 640 232 L640 445 L0 445 Z" fill="var(--sky)"/>
    <path d="M0 278 C200 262 470 290 650 238 L760 0 L1123 0 L1123 445 L0 445 Z" fill="var(--blue)"/>
    <path d="M1020 270 L1123 372 L1123 445 L1095 445 L960 360 Z" fill="url(#handleGrad)"/>
    <circle cx="844" cy="209" r="216" fill="url(#ringGrad)"/>
  </svg>
  <div class="photo" role="img" aria-label="Photo of a support worker in a white coat and face mask, holding a stethoscope"></div>
  <div class="brand"><span class="brand-dot"></span>Kestrel Path</div>

  <span class="accent-bar"></span>
  <h1 class="headline"><span class="lead">STOP CLAPPING –</span><span class="strong">JOIN THE FRONTLINE</span></h1>
  <span class="divider"></span>
  <p class="role">SUPPORT WORKER JOBS</p>
  <p class="cta-line">APPLY NOW. MAKE A DIFFERENCE</p>
  <p class="more-pill">FIND OUT MORE ABOUT US AT</p>

  <div class="phone">
    <svg width="44" height="44" viewBox="0 0 24 24" aria-hidden="true"><path fill="var(--gold)" d="M6.6 10.8a15.1 15.1 0 0 0 6.6 6.6l2.2-2.2c.3-.3.7-.4 1-.2 1.1.4 2.3.6 3.6.6.6 0 1 .4 1 1V20c0 .6-.4 1-1 1C10.6 21 3 13.4 3 4c0-.6.4-1 1-1h3.5c.6 0 1 .4 1 1 0 1.3.2 2.5.6 3.6.1.3 0 .7-.2 1z"/><path fill="none" stroke="var(--gold)" stroke-width="1.6" stroke-linecap="round" d="M14.5 3.5a6.5 6.5 0 0 1 6 6M14.5 7a3 3 0 0 1 2.6 2.6"/></svg>
    <span>0800 712 4093</span>
  </div>
  <span class="contact-rule"></span>
  <ul class="contacts">
    <li><svg width="18" height="18" viewBox="0 0 24 24" aria-hidden="true"><g fill="none" stroke="var(--gold)" stroke-width="2"><circle cx="12" cy="12" r="9"/><path d="M3 12h18M12 3c3 3 3 15 0 18M12 3c-3 3-3 15 0 18"/></g></svg>www.kestrelpathlimited.co.uk</li>
    <li><svg width="18" height="14" viewBox="0 0 24 18" aria-hidden="true"><rect width="24" height="18" fill="var(--gold)"/><path d="M1 1l11 8 11-8" fill="none" stroke="var(--blue)" stroke-width="2"/></svg>support@kestrelpathgroup.co.uk</li>
  </ul>
</section>
</body>
</html>
```